Wellbeing Challenge Posters

We are running a wellbeing challenge. Every week we run a challenge under a different theme. We need 5 themes to start with:
- Connect
- Be mindful
- Get moving
- Give
- Grow your mind

Each theme needs to have the following:
1. Match the colours of the icons provided under each
2. Have a clear place for the word where these can be changed but utilising the same theme. For example, under connect, we will run a number of different challenges but the theme will remain the same.
3. Each theme will have the following:
-This week's challenge
- Points
4. The Thrive Challenge logo

The content under each of the themes will be as follows:

1. Connect
This week's challenge: Have a shared meal with your team - take a photo and post it on the challenge forum
Points: 10 points per person that attended if you had more than 75% of your team

2. Be Mindful
This week's challenge: START something that will improve your wellbeing, STOP something that is bad for you - Be mindful of how you feel at the end of the week.

3. Get moving:
This week's challenge: Do a minimum 150 minutes of exercise this week required for good general health - try something new!
Points: Take your usual 1 point per 30 mins exercise but give yourself an additional 10 points if you do 150mins or more for the week.

4. Give:
This week's challenge: Do a random act of kindness every day this week
Points: 1 point per day PLUS 10 points if you complete 1 every day

5. Grow Your Mind
This week's challenge: Learn something new every day! Read a research paper, watch a ZIVO talk, DIY, learn something about your workmates

```html
<!DOCTYPE html>
<html lang="en">
<head>
<meta charset="utf-8">
<title>Connect – Weekly Challenge Poster</title>
<link href="https://fonts.googleapis.com/css2?family=Arvo:wght@700&family=Bebas+Neue&family=Open+Sans:wght@400;600;700&display=swap" rel="stylesheet">
<style>
  :root {
    --teal: #1aaab5;
    --teal-deep: #16a3ad;
    --teal-soft: #8ccfd7;
    --orange: #dd5b36;
    --ink: #4a4a4a;
    --white: #ffffff;
    --stripe: #9fd3da;
    --brand-grey: #555a5e;
  }
  * { margin: 0; padding: 0; box-sizing: border-box; }
  html, body { width: 987px; height: 1200px; overflow: hidden; background: #ffffff; }
  .poster {
    position: relative;
    width: 987px;
    height: 1200px;
    overflow: hidden;
    background:
      radial-gradient(ellipse 360px 300px at 495px 330px, rgba(255,255,255,0.55), rgba(255,255,255,0) 70%),
      linear-gradient(180deg, var(--teal) 0%, #5dbfc8 30%, var(--teal-soft) 52%, #d6eef1 68%, var(--white) 80%);
    font-family: "Open Sans", sans-serif;
  }
  .theme-title { position: absolute; left: 0; top: 0; width: 987px; height: 300px; }
  .theme-title text {
    font-family: "Arvo", serif;
    font-weight: 700;
    font-size: 100px;
    fill: var(--white);
    letter-spacing: 2px;
  }
  .theme-icon {
    position: absolute;
    left: 218px; top: 265px;
    width: 536px; height: 222px;
    border-radius: 110px;
    background: linear-gradient(180deg, #e0663f 0%, #e0663f 32%, #a9d45a 55%, #4fc28f 100%);
    border: 10px solid var(--white);
    box-shadow: 0 0 0 9px var(--teal-deep);
  }
  .theme-tagline {
    position: absolute; left: 0; top: 490px; width: 987px;
    text-align: center;
    font-weight: 700; font-size: 57px;
    color: var(--orange);
  }
  .challenge-ribbon { position: absolute; left: 63px; top: 608px; width: 858px; height: 70px; }
  .challenge-heading {
    position: absolute; left: 63px; top: 610px; width: 858px; height: 64px;
    display: flex; align-items: center; justify-content: center;
    font-family: "Bebas Neue", sans-serif; font-weight: 400; font-size: 54px; letter-spacing: 3px;
    color: var(--white);
  }
  .challenge-text {
    position: absolute; left: 0; top: 686px; width: 987px;
    text-align: center;
    font-size: 35px; line-height: 45px;
    color: var(--ink);
  }
  .points-box {
    position: absolute; left: 111px; top: 842px; width: 769px; height: 149px;
    border: 3px solid var(--orange);
    border-top: none;
  }
  .points-rule {
    position: absolute; top: 0; height: 3px; background: var(--orange);
  }
  .points-rule.left { left: -3px; width: 258px; }
  .points-rule.right { left: 509px; width: 257px; }
  .points-heading {
    position: absolute; left: 0; top: -32px; width: 100%;
    text-align: center;
    font-family: "Bebas Neue", sans-serif; font-weight: 400; font-size: 56px; letter-spacing: 2px;
    color: var(--orange); line-height: 62px;
  }
  .points-text {
    position: absolute; left: 0; top: 40px; width: 100%;
    text-align: center;
    font-size: 36px; line-height: 44px;
    color: var(--teal-deep);
  }
  .contact-band { position: absolute; left: 0; top: 1063px; width: 620px; height: 137px; }
  .contact-heading {
    position: absolute; left: 24px; top: 1079px;
    font-family: "Bebas Neue", sans-serif; font-weight: 400; font-size: 37px;
    color: var(--white);
  }
  .contact-line {
    position: absolute; left: 22px;
    display: flex; align-items: center; gap: 12px;
    font-size: 23px; color: var(--white);
  }
  .contact-line.phone { top: 1122px; }
  .contact-line.web { top: 1157px; }
  .contact-icon { width: 30px; height: 30px; }
  .brand-name {
    position: absolute; left: 640px; top: 1112px; width: 320px;
    text-align: center;
    font-weight: 600; font-size: 26px;
    color: var(--brand-grey);
  }
</style>
</head>
<body>
<main class="poster">

  <svg class="theme-title" viewBox="0 0 987 300" aria-label="Connect">
    <defs>
      <path id="title-arc" d="M 170 262 A 800 800 0 0 1 815 262"/>
    </defs>
    <text><textPath href="#title-arc" startOffset="50%" text-anchor="middle">CONNECT</textPath></text>
  </svg>

  <div class="theme-icon" role="img" aria-label="Connect theme icon: three linked figures in orange and green"></div>

  <p class="theme-tagline">Engage with others</p>

  <svg class="challenge-ribbon" viewBox="0 0 858 70" preserveAspectRatio="none" aria-hidden="true">
    <polygon points="0,0 858,0 839,33 858,70 0,70 19,33" fill="#16a3ad"/>
    <rect x="10" y="66" width="838" height="4" fill="#0f7f88" opacity="0.35"/>
  </svg>
  <h2 class="challenge-heading">This Week's Challenge</h2>

  <p class="challenge-text">Have a shared meal with your team<br>take a photo and post it on the challenge forum</p>

  <section class="points-box">
    <span class="points-rule left"></span>
    <span class="points-rule right"></span>
    <h3 class="points-heading">Points</h3>
    <p class="points-text">10 points per person that attended<br>if you had more than 75% of your team</p>
  </section>

  <svg class="contact-band" viewBox="0 0 620 137" aria-hidden="true">
    <polygon points="500,0 530,0 604,137 574,137" fill="#9fd3da"/>
    <polygon points="0,0 500,0 574,137 0,137" fill="#dd5b36"/>
  </svg>
  <h4 class="contact-heading">Contact us now to register your team</h4>
  <p class="contact-line phone">
    <svg class="contact-icon" viewBox="0 0 30 30" aria-hidden="true">
      <circle cx="15" cy="15" r="14" fill="#ffffff"/>
      <path d="M10 8 l3 0 l1.5 4 l-2 1.5 a9 9 0 0 0 4 4 l1.5 -2 l4 1.5 l0 3 a2 2 0 0 1 -2 2 a13 13 0 0 1 -12 -12 a2 2 0 0 1 2 -2z" fill="#dd5b36"/>
    </svg>
    04 218 5390
  </p>
  <p class="contact-line web">
    <svg class="contact-icon" viewBox="0 0 30 30" aria-hidden="true">
      <circle cx="15" cy="15" r="14" fill="#ffffff"/>
      <g fill="none" stroke="#dd5b36" stroke-width="1.4">
        <circle cx="15" cy="15" r="8"/>
        <ellipse cx="15" cy="15" rx="3.5" ry="8"/>
        <line x1="7" y1="15" x2="23" y2="15"/>
        <line x1="8.5" y1="11" x2="21.5" y2="11"/>
        <line x1="8.5" y1="19" x2="21.5" y2="19"/>
      </g>
    </svg>
    fieldwellness.co.nz
  </p>

  <p class="brand-name">The Thrive Challenge</p>

</main>
</body>
</html>
```